Business card design for engineering firm specializing in defense industry.

We need a professional business card design. Something simple but stands out. We are an engineering company specializing in composites in the defense industry.
Industry/Entity Type
Defense
Contact Information for Business Card
A simple black business card with the Varlonix yellow color is what we had in mind but open for other designs.
Colors
ffc214

```html
<!DOCTYPE html>
<html lang="en">
<head>
<meta charset="utf-8">
<title>Varlonix Business Card</title>
<link href="https://fonts.googleapis.com/css2?family=Roboto:wght@300;400;500;700&display=swap" rel="stylesheet">
<style>
  :root {
    --brand-yellow: #ffc214;
    --ink: #111111;
    --text-grey: #555555;
    --card-white: #ffffff;
    --backdrop: #e9e6e2;
    --rule: #333333;
  }
  * { margin: 0; padding: 0; box-sizing: border-box; }
  html, body { width: 1125px; height: 1200px; overflow: hidden; }
  body {
    background: var(--backdrop);
    font-family: "Roboto", Arial, sans-serif;
    position: relative;
  }
  .card {
    position: absolute;
    left: 150px;
    width: 825px;
    height: 471px;
    overflow: hidden;
  }
  .card-front { top: 98px; background: var(--card-white); }
  .card-back { top: 631px; }

  .brand-lockup {
    position: absolute;
    left: 225px;
    top: 305px;
    display: flex;
    align-items: center;
    gap: 14px;
  }
  .brand-lockup .brand-square {
    width: 30px; height: 30px;
    background: var(--brand-yellow);
  }
  .brand-lockup .brand-name {
    font-size: 48px;
    font-weight: 700;
    color: var(--ink);
    letter-spacing: 0.5px;
    line-height: 1;
  }

  .divider {
    position: absolute;
    left: 452px;
    top: 107px;
    width: 1px;
    height: 257px;
    background: var(--rule);
  }
  .contact-block {
    position: absolute;
    left: 491px;
    top: 102px;
  }
  .person-name {
    font-size: 31px;
    font-weight: 500;
    color: var(--ink);
    line-height: 1.1;
  }
  .person-title {
    font-size: 22px;
    font-weight: 400;
    color: var(--brand-yellow);
    line-height: 1.1;
    margin-top: 1px;
  }
  .address {
    margin-top: 13px;
    font-size: 19px;
    font-weight: 300;
    color: var(--text-grey);
    line-height: 25px;
  }
  .contact-list {
    list-style: none;
    margin-top: 14px;
  }
  .contact-list li {
    display: flex;
    align-items: center;
    height: 26px;
    font-size: 19px;
    font-weight: 300;
    color: var(--text-grey);
  }
  .contact-list svg {
    width: 17px; height: 17px;
    margin-right: 14px;
    fill: var(--ink);
    flex: none;
  }
  .front-stripe {
    position: absolute;
    left: 0; right: 0;
    top: 455px;
    height: 3px;
    background: var(--brand-yellow);
  }
  .front-base {
    position: absolute;
    left: 0; right: 0;
    top: 459px;
    bottom: 0;
    background: var(--ink);
  }

  .back-texture {
    position: absolute;
    inset: 0;
    background:
      linear-gradient(180deg, rgba(255,194,20,0.10), rgba(255,194,20,0.06)),
      linear-gradient(100deg, #050505 0%, #0d0d0d 55%, #2c2c2c 100%);
  }
  .back-mark {
    position: absolute;
    right: 66px;
    bottom: 62px;
    display: flex;
    align-items: center;
    gap: 10px;
  }
  .back-mark .brand-square {
    width: 22px; height: 22px;
    background: var(--brand-yellow);
  }
  .back-mark .brand-name {
    font-size: 30px;
    font-weight: 700;
    color: var(--brand-yellow);
    line-height: 1;
  }
</style>
</head>
<body>

<section class="card card-front">
  <div class="brand-lockup">
    <span class="brand-square"></span>
    <span class="brand-name">Varlonix</span>
  </div>

  <div class="divider"></div>

  <div class="contact-block">
    <h1 class="person-name">Daniel Mercer</h1>
    <p class="person-title">Founder</p>
    <p class="address">4120 Alder Court<br>Kenmore, Alaska 34581</p>
    <ul class="contact-list">
      <li>
        <svg viewBox="0 0 24 24" aria-hidden="true"><path d="M6.6 10.8c1.4 2.8 3.8 5.1 6.6 6.6l2.2-2.2c.3-.3.7-.4 1-.2 1.1.4 2.3.6 3.6.6.6 0 1 .4 1 1V20c0 .6-.4 1-1 1C10.6 21 3 13.4 3 4c0-.6.4-1 1-1h3.5c.6 0 1 .4 1 1 0 1.3.2 2.5.6 3.6.1.3 0 .7-.2 1z"/></svg>
        555 214 7830
      </li>
      <li>
        <svg viewBox="0 0 24 24" aria-hidden="true"><path d="M7 1h10a2 2 0 0 1 2 2v18a2 2 0 0 1-2 2H7a2 2 0 0 1-2-2V3a2 2 0 0 1 2-2zm0 3v14h10V4zm5 15.5a1 1 0 1 0 0 2 1 1 0 0 0 0-2z"/></svg>
        555 390 1627
      </li>
      <li>
        <svg viewBox="0 0 24 24" aria-hidden="true"><path d="M7 2h10v5H7zM3 8h18a1 1 0 0 1 1 1v8h-4v5H6v-5H2V9a1 1 0 0 1 1-1zm5 8v4h8v-4z"/></svg>
        555 762 4418
      </li>
      <li>
        <svg viewBox="0 0 24 24" aria-hidden="true"><path d="M2 5h20v14H2zm2 2v.5l8 5.5 8-5.5V7l-8 5.5z"/></svg>
        daniel@varlonix.com
      </li>
      <li>
        <svg viewBox="0 0 24 24" aria-hidden="true"><path d="M12 2a10 10 0 1 0 0 20 10 10 0 0 0 0-20zm-1 3.5c-1.6.8-2.4 2-2 3.3.5 1.5 2.3 1.4 2.6 3 .3 1.4-1.5 2-1.3 3.6.2 1.4 1.3 2.3 1 3.8A8 8 0 0 1 4.4 9.6zm4.5 1.2A8 8 0 0 1 19.6 16c-.8-1-2-1.2-2.8-2.2-.9-1.2.2-2.7-.8-3.9-.6-.8-1.7-.6-2.1-1.6-.2-.6.4-1.3 1.6-1.8z"/></svg>
        www.varlonix.com
      </li>
    </ul>
  </div>

  <div class="front-stripe"></div>
  <div class="front-base"></div>
</section>

<section class="card card-back">
  <div class="back-texture" role="img" aria-label="Repeating faint yellow geometric brand pattern on black"></div>
  <div class="back-mark">
    <span class="brand-square"></span>
    <span class="brand-name">Varlonix</span>
  </div>
</section>

</body>
</html>
```